Merry Fern Lumo alcohol cooler

I need a design using my Merry Fern Beverage Logo for 4 different styles of Malt Beverage. The cocktails are easy drinking tropical feel. We will be using the best ingredients and try to be all natural and organic.
Zaller Lime
Zaller Orange
Zaller Grapefruit
Zaller Strawberry
We would like as few colors as possible in the design.

Target Market(s)

21 - 50
Women

Requirements
Must have
• the 4 styles
• my LOGO
• label dimension inside 3"wide x 4"high maximum
• 4 pack design
• label must have 12 FL OZ
• label must have 5% ALC/VOL
Nice to have
• Clean crisp feel
Should not have
• please keep design to 3 colors or less

```html
<!DOCTYPE html>
<html lang="en">
<head>
<meta charset="utf-8">
<title>Zaller by Merry Fern Beverage – Label Range</title>
<link rel="stylesheet" href="https://fonts.googleapis.com/css2?family=Fira+Sans:wght@600;700&display=swap">
<style>
  :root {
    --canvas: #ffffff;
    --white: #ffffff;
    --orange: #f07a2a;
    --orange-tint: #f6c9a4;
    --lime: #3f9f52;
    --lime-tint: #b9e27c;
    --strawberry: #d9413f;
    --strawberry-tint: #f2a3a0;
    --grapefruit: #8c2f63;
    --grapefruit-tint: #e4b3cf;
  }
  * { box-sizing: border-box; margin: 0; padding: 0; }
  html, body {
    width: 1200px;
    height: 1000px;
    overflow: hidden;
    background: var(--canvas);
  }
  .label-range {
    width: 1200px;
    height: 1000px;
    display: flex;
    justify-content: center;
    align-items: center;
    gap: 40px;
    font-family: "Fira Sans", Arial, sans-serif;
  }
  .label {
    width: 255px;
    height: 340px;
    background: var(--tint);
    border-radius: 6px;
    display: flex;
    flex-direction: column;
    align-items: center;
    justify-content: center;
    padding: 20px 10px;
  }
  .label--orange { --main: var(--orange); --tint: var(--orange-tint); }
  .label--lime { --main: var(--lime); --tint: var(--lime-tint); }
  .label--strawberry { --main: var(--strawberry); --tint: var(--strawberry-tint); }
  .label--grapefruit { --main: var(--grapefruit); --tint: var(--grapefruit-tint); }

  .brand-mark {
    width: 180px;
    height: 180px;
    border-radius: 50%;
    background: var(--main);
    display: flex;
    align-items: center;
    justify-content: center;
    text-align: center;
    padding: 24px;
  }
  .brand-name {
    color: var(--white);
    font-weight: 600;
    font-size: 22px;
    line-height: 1.2;
    letter-spacing: 2px;
    text-transform: uppercase;
  }
  .flavour-band {
    margin-top: 26px;
    background: var(--main);
    color: var(--white);
    font-weight: 700;
    font-size: 25px;
    letter-spacing: 0.5px;
    text-transform: uppercase;
    padding: 5px 10px 4px;
    white-space: nowrap;
  }
  .volume-tag {
    background: var(--main);
    color: var(--white);
    font-weight: 600;
    font-size: 10px;
    letter-spacing: 0.5px;
    padding: 2px 8px;
  }
</style>
</head>
<body>
  <main class="label-range">
    <article class="label label--orange">
      <div class="brand-mark"><span class="brand-name">Merry Fern Beverage</span></div>
      <h2 class="flavour-band">Zaller Orange</h2>
      <p class="volume-tag">12 FL OZ 5% ALC/VOL</p>
    </article>
    <article class="label label--lime">
      <div class="brand-mark"><span class="brand-name">Merry Fern Beverage</span></div>
      <h2 class="flavour-band">Zaller Lime</h2>
      <p class="volume-tag">12 FL OZ 5% ALC/VOL</p>
    </article>
    <article class="label label--strawberry">
      <div class="brand-mark"><span class="brand-name">Merry Fern Beverage</span></div>
      <h2 class="flavour-band">Zaller Strawberry</h2>
      <p class="volume-tag">12 FL OZ 5% ALC/VOL</p>
    </article>
    <article class="label label--grapefruit">
      <div class="brand-mark"><span class="brand-name">Merry Fern Beverage</span></div>
      <h2 class="flavour-band">Zaller Grapefruit</h2>
      <p class="volume-tag">12 FL OZ 5% ALC/VOL</p>
    </article>
  </main>
</body>
</html>
```